Veltrano - Mechanic/Collision Center Business Card

We're looking for a business card design for our mechanic/ collision repair shop.

Can be with colours or monochromatic.

See the attached files.

Many thanks

```html
<!DOCTYPE html>
<html lang="pt">
<head>
<meta charset="utf-8">
<title>Veltrano – Business Card</title>
<link href="https://fonts.googleapis.com/css2?family=Montserrat:wght@500;600;700;800&display=swap" rel="stylesheet">
<style>
  :root {
    --bg: #34464d;
    --yellow: #fee660;
    --yellow-light: #fff38a;
    --yellow-text: #f5e63a;
    --ink: #231f20;
    --grey: #e9e9eb;
    --photo-dark: #4a4a44;
    --photo-mid: #c99a1e;
    --photo-light: #e8e6e0;
  }
  * { margin: 0; padding: 0; box-sizing: border-box; }
  html, body {
    width: 1200px; height: 900px; overflow: hidden;
    background: var(--bg);
    font-family: "Montserrat", sans-serif;
  }
  .card {
    position: absolute; left: 190px; width: 820px; height: 420px;
    overflow: hidden; background: var(--yellow);
    box-shadow: 0 10px 24px rgba(0,0,0,.35);
  }
  .card--front { top: 22px; }
  .card--back { top: 462px; }
  .card__shapes { position: absolute; inset: 0; }

  .company-name {
    position: absolute; left: 40px; top: 72px;
    font-size: 36px; font-weight: 800; color: var(--ink);
  }
  .company-name small { font-size: 24px; font-weight: 500; }

  .brand-tab {
    position: absolute; left: 590px; top: 58px; width: 230px; height: 100px;
    display: flex; align-items: center; justify-content: center;
    font-size: 30px; font-weight: 800; color: var(--ink); letter-spacing: 1px;
  }

  .contact { position: absolute; list-style: none; color: var(--yellow-text); font-weight: 500; }
  .contact li { position: relative; padding-left: 28px; font-size: 19px; line-height: 1.25; margin-bottom: 18px; }
  .contact li::before {
    content: ""; position: absolute; left: 0; top: 7px; width: 14px; height: 12px;
    background: var(--yellow-text);
  }
  .contact--left { left: 44px; top: 184px; }
  .contact--right { left: 574px; top: 190px; }
  .contact--right li { margin-bottom: 14px; }

  .manager {
    position: absolute; left: 28px; top: 360px; right: 20px;
    display: flex; align-items: flex-start; color: var(--ink);
    font-weight: 700; font-size: 18px;
  }
  .manager__label { position: relative; padding-left: 28px; margin-top: 14px; width: 430px; }
  .manager__label::before {
    content: ""; position: absolute; left: 0; top: 5px; width: 16px; height: 13px; background: var(--ink);
  }
  .manager__contact { line-height: 1.35; }

  .photo-area {
    position: absolute; left: 0; top: 0; width: 330px; height: 420px;
    background: linear-gradient(160deg, var(--photo-light) 0%, var(--photo-mid) 45%, var(--photo-dark) 100%);
  }
  .brand-mark {
    position: absolute; left: 420px; right: 20px; top: 0; bottom: 0;
    display: flex; align-items: center; justify-content: center;
    font-size: 64px; font-weight: 800; color: var(--ink); letter-spacing: 2px;
  }
</style>
</head>
<body>

<section class="card card--front">
  <svg class="card__shapes" viewBox="0 0 820 420" width="820" height="420">
    <rect x="0" y="0" width="820" height="50" fill="var(--yellow-light)"/>
    <rect x="0" y="150" width="820" height="195" fill="var(--ink)"/>
    <polygon points="600,40 820,40 820,178 620,178 596,150 580,150 580,70" fill="var(--yellow)"/>
  </svg>

  <h1 class="company-name">Veltrano, <small>LDA</small></h1>
  <div class="brand-tab">VELTRANO</div>

  <ul class="contact contact--left">
    <li>veltrano.oficina@mailbox.pt</li>
    <li>Rua das Oficinas, 42</li>
    <li>www.veltrano-auto.pt</li>
  </ul>
  <ul class="contact contact--right">
    <li>351 210000417<br>210000417</li>
    <li>1900-214 Lisboa</li>
  </ul>

  <div class="manager">
    <span class="manager__label">Manager Mobile Number:</span>
    <span class="manager__contact">Rui Matos<br>+351 912000358 &nbsp;/&nbsp; 912000358</span>
  </div>
</section>

<section class="card card--back">
  <div class="photo-area" role="img" aria-label="Photograph of the front of a yellow sports car"></div>
  <svg class="card__shapes" viewBox="0 0 820 420" width="820" height="420">
    <polygon points="330,0 360,0 360,70 388,80 388,330 360,420 320,420" fill="var(--grey)"/>
  </svg>
  <div class="brand-mark">VELTRANO</div>
</section>

</body>
</html>
```